Biz card for my counselling/social work practice

Biz card design for my counselling practice, focus on well-being, I am a social worker who also teaches meditation and workshops but my main focus for the card is my counselling practice. My website reveals a gentle flowing quality which I would life reflected in my card. This business card will be designed to share with other practitioners who are looking for support with their clients to take their healing to another level or well-being.

Target Market(s)

professionals seeking mental health counselling/men/women/ those seeking to improve their well-being through insight based counselling to optimize their lives and process trauma or limiting patterns

Industry/Entity Type

Counsellor

Contact Information for Business Card

Info on the card: perhaps text is aligned left?
Maribel Strand, MSW, RSW
Counsellor
614.295.3140
info@maribelstrand.example
www.maribelstrand.example

Please use a modern font doesn’t need to be the one chosen below. Thank you

Font styles to use
Serif

Colors
3176b5
33a6d7
33b8a4
6b449b
abd037
d2a4cc
e55fa2

Requirements
Must have
• My business card details on front
• Backside
• Accelerated Resolution Therapy
• Cognitive Behavioral Therapy
• Mindfulness Informed Therapy
Nice to have
• I would like the card to be basic, (white or creme without too much bold colour) and with perhaps a stripe or band of vertical colour in blue or green (or a merge of colour) perhaps embossed or in a negative space. (this is one idea, but do not want the card to be too feminine or interest only women as i see men too so this is only an idea, but not 100 percent on this.
• I do not have a logo. I would prefer to heart from my website not to be used in the design as i am considering modifying this and re-branding.
Should not have
• too bold colours or bright yellow/blacks. i Like tones that are greens, blues.

```html
<!DOCTYPE html>
<html lang="en">
<head>
<meta charset="utf-8">
<title>Maribel Strand – Business Card</title>
<link rel="stylesheet" href="https://fonts.googleapis.com/css2?family=Open+Sans:wght@400&family=Source+Serif+4:wght@300;400&display=swap">
<style>
  :root {
    --page-bg: #f5f5f5;
    --card-bg: #ffffff;
    --ink-label: #1c1c1c;
    --ink-grey: #707070;
    --ink-blue: #3176b5;
    --band-blue: #34a5d6;
    --band-green: #33b8a4;
    --heart-pink: #e55fa2;
    --ink-white: #ffffff;
  }
  * { box-sizing: border-box; margin: 0; padding: 0; }
  html, body { width: 899px; height: 1200px; overflow: hidden; }
  body {
    background: var(--page-bg);
    position: relative;
    font-family: "Source Serif 4", Georgia, serif;
  }
  .side-label {
    position: absolute;
    left: 0; width: 899px;
    text-align: center;
    font-family: "Open Sans", Arial, sans-serif;
    font-size: 32px;
    color: var(--ink-label);
    line-height: 1;
  }
  .side-label--front { top: 58px; }
  .side-label--back { top: 642px; }

  .card {
    position: absolute;
    width: 766px; height: 449px;
    background: var(--card-bg);
    overflow: hidden;
  }
  .card--front { left: 67px; top: 120px; }
  .card--back { left: 63px; top: 698px; }

  .card__band { position: absolute; left: 0; top: 0; width: 766px; height: 449px; }

  .identity {
    position: absolute; left: 0; top: 0; width: 100%;
    text-align: center;
    color: var(--ink-grey);
  }
  .identity__name {
    position: absolute; left: 0; width: 100%; top: 212px;
    font-size: 39px; font-weight: 400; line-height: 1;
  }
  .identity__role {
    position: absolute; left: 0; width: 100%; top: 258px;
    font-size: 31px; font-weight: 300; color: var(--ink-blue); line-height: 1;
  }
  .identity__phone {
    position: absolute; left: 0; width: 100%; top: 338px;
    font-size: 27px; font-weight: 300; line-height: 1;
  }
  .card--front .identity { top: -120px; }

  .contact {
    position: absolute; left: 0; top: 356px; width: 100%;
    display: flex; justify-content: center; align-items: center; gap: 14px;
    color: var(--ink-white);
    font-size: 21px; line-height: 1;
  }
  .heart { display: block; fill: var(--heart-pink); }

  .services {
    position: absolute; left: 107px; top: 92px;
    list-style: none;
  }
  .services__item {
    display: flex; align-items: center; gap: 18px;
    height: 52px;
    font-size: 31px; font-weight: 300; color: var(--ink-grey);
  }
</style>
</head>
<body>
  <div class="side-label side-label--front">FRONT</div>
  <section class="card card--front">
    <svg class="card__band" viewBox="0 0 766 449" role="img" aria-label="Flowing blue band with faint script texture">
      <path d="M0 270 Q383 342 766 274 L766 449 L0 449 Z" fill="var(--band-green)"/>
      <path d="M0 278 Q383 350 766 283 L766 449 L0 449 Z" fill="var(--band-blue)"/>
    </svg>
    <div class="identity">
      <h1 class="identity__name">Maribel Strand, MSW, RSW</h1>
      <p class="identity__role">Counsellor</p>
      <p class="identity__phone">614.295.3140</p>
    </div>
    <div class="contact">
      <span class="contact__email">info@maribelstrand.example</span>
      <svg class="heart" width="24" height="22" viewBox="0 0 24 22"><path d="M12 21S2 14.5 2 7.5A5 5 0 0 1 12 5a5 5 0 0 1 10 2.5C22 14.5 12 21 12 21z"/></svg>
      <span class="contact__web">www.maribelstrand.example</span>
    </div>
  </section>

  <div class="side-label side-label--back">BACK</div>
  <section class="card card--back">
    <svg class="card__band" viewBox="0 0 766 449" role="img" aria-label="Flowing blue band with faint script texture">
      <path d="M0 270 Q383 342 766 274 L766 449 L0 449 Z" fill="var(--band-green)"/>
      <path d="M0 278 Q383 350 766 283 L766 449 L0 449 Z" fill="var(--band-blue)"/>
    </svg>
    <ul class="services">
      <li class="services__item"><svg class="heart" width="24" height="22" viewBox="0 0 24 22"><path d="M12 21S2 14.5 2 7.5A5 5 0 0 1 12 5a5 5 0 0 1 10 2.5C22 14.5 12 21 12 21z"/></svg>Accelerated Resolution Therapy</li>
      <li class="services__item"><svg class="heart" width="24" height="22" viewBox="0 0 24 22"><path d="M12 21S2 14.5 2 7.5A5 5 0 0 1 12 5a5 5 0 0 1 10 2.5C22 14.5 12 21 12 21z"/></svg>Cognitive Behavioral Therapy</li>
      <li class="services__item"><svg class="heart" width="24" height="22" viewBox="0 0 24 22"><path d="M12 21S2 14.5 2 7.5A5 5 0 0 1 12 5a5 5 0 0 1 10 2.5C22 14.5 12 21 12 21z"/></svg>Mindfulness Informed Therapy</li>
    </ul>
    <div class="contact">
      <span class="contact__email">info@maribelstrand.example</span>
      <svg class="heart" width="24" height="22" viewBox="0 0 24 22"><path d="M12 21S2 14.5 2 7.5A5 5 0 0 1 12 5a5 5 0 0 1 10 2.5C22 14.5 12 21 12 21z"/></svg>
      <span class="contact__web">www.maribelstrand.example</span>
    </div>
  </section>
</body>
</html>
```